Vision / Mission Poster Required

We are looking to display our company Vision / Mission / Values on a poster. This will be displayed in the head office and other site offices.

The document needs to look professional however still be fun, eye catching and easy to read. It will be predominantly displayed in A3 format.

The design needs to use our company Logo which is attached along with the Text to display on the poster. I have put some additional text on the doc that you can include if it suits the layout but is not essential.

Target Market(s)

Staff, Corporate Visitors

Industry/Entity Type

Electric Company

Font styles to use
Sans Serif

Colors

Designer to choose colors to be used in the design.

Requirements
Must have
• Incorporate Logo
• Professional Look
• Attention grabbing
• Easy to Read
Should not have
• Lightning Bolts
• Pictures of random people/Things

```html
<!DOCTYPE html>
<html lang="en">
<head>
<meta charset="utf-8">
<title>Brightline Electrical – Mission &amp; Values</title>
<link rel="stylesheet" href="https://fonts.googleapis.com/css2?family=Fira+Sans+Condensed:wght@600&family=Open+Sans:wght@400;600;700&display=swap">
<style>
  :root {
    --navy: #1b355f;
    --navy-text: #1d3a6b;
    --gold: #fcc70f;
    --gold-text: #fbbf24;
    --orange-1: #ef6c35;
    --orange-2: #f59a3c;
    --orange-3: #fbbd3e;
    --ink: #1c1c1c;
    --white: #ffffff;
  }
  * { box-sizing: border-box; margin: 0; padding: 0; }
  html, body { width: 1200px; height: 1200px; overflow: hidden; background: var(--white); }
  body { font-family: "Open Sans", Arial, sans-serif; color: var(--ink); position: relative; }

  .hero {
    position: absolute; left: 182px; top: 20px; width: 818px; height: 374px;
    background:
      linear-gradient(90deg, rgba(40,30,20,0.85) 0%, rgba(90,70,50,0.6) 30%, rgba(0,0,0,0) 50%),
      linear-gradient(180deg, #d8b040 0%, #6b5a48 40%, #b9aa98 100%),
      #8a7a6a;
  }
  .hero__art {
    position: absolute; left: 400px; top: 0; width: 418px; height: 100%;
    background: linear-gradient(135deg, #f4c23a 0%, #e94f6b 30%, #2fa6c9 55%, #f07ab0 75%, #f3a23a 100%);
  }
  .hero__title {
    position: absolute; left: 213px; top: 340px;
    font-family: "Fira Sans Condensed", "Arial Narrow", sans-serif; font-weight: 600;
    font-size: 35px; line-height: 1.1; color: #111; letter-spacing: -0.2px; white-space: nowrap;
  }

  .accent-bar { position: absolute; left: 944px; top: 402px; width: 56px; height: 16px; background: var(--navy); }

  .gallery__frame {
    position: absolute; left: 792px; width: 150px; background: var(--white); padding: 10px;
  }
  .gallery__frame span { display: block; width: 100%; height: 100%; }

  .values {
    position: absolute; left: 500px; top: 408px; width: 500px; height: 568px;
    background: var(--navy); color: var(--white);
  }
  .values__title {
    position: absolute; left: 26px; top: 28px; font-size: 21px; font-weight: 700; color: var(--gold-text);
  }
  .value { position: absolute; left: 26px; }
  .value h3 { font-size: 18.5px; font-weight: 700; line-height: 1.2; margin-bottom: 2px; }
  .value p { font-size: 14.6px; line-height: 19.5px; }

  .brand {
    position: absolute; left: 200px; top: 446px; display: flex; align-items: center; gap: 14px;
  }
  .brand__mark { width: 60px; height: 60px; border-radius: 50%; background: var(--orange-1); flex: none; }
  .brand__name { font-size: 34px; font-weight: 700; color: var(--navy-text); line-height: 1.02; }

  .mission__title { position: absolute; left: 234px; top: 586px; font-size: 22px; font-weight: 700; color: #222; }
  .goal { position: absolute; left: 182px; width: 310px; }
  .goal__num {
    position: absolute; left: 0; top: 0; width: 44px; height: 100%;
    color: var(--white); font-size: 28px; font-weight: 700;
    display: flex; align-items: center; justify-content: center;
  }
  .goal__text { margin-left: 51px; }
  .goal__text h3 { font-size: 16.5px; font-weight: 700; line-height: 20px; }
  .goal__text p { font-size: 14.5px; line-height: 20.5px; }

  .statement {
    position: absolute; left: 170px; top: 984px; width: 830px; height: 196px;
    background: var(--gold); color: var(--navy-text); padding: 18px 22px 0 38px;
    font-size: 14.8px; line-height: 18.8px;
  }
  .statement p + p { margin-top: 4px; }
</style>
</head>
<body>

  <div class="hero" role="img" aria-label="Photo of a busy shopping arcade with a colourful mural wall">
    <div class="hero__art"></div>
  </div>
  <h1 class="hero__title">Dynamic results- Proven reputation</h1>

  <div class="accent-bar"></div>

  <div class="values">
    <h2 class="values__title">VALUES</h2>
    <div class="value" style="top:66px; width:262px;">
      <h3>Honesty &amp;Integrity</h3>
      <p>Customers, contractors and suppliers will be able to count on Brightline personnel to deal straightforwardly and adhere to the strictest moral and ethical codes of conduct.</p>
    </div>
    <div class="value" style="top:224px; width:462px;">
      <h3>Safety &amp; Responsibility</h3>
      <p>Brightline is committed to constantly improving safety practices at project job sites and within the electrical service industry as a whole.</p>
    </div>
    <div class="value" style="top:322px; width:450px;">
      <h3>Commitment to Quality</h3>
      <p>Customers and stakeholders will be able to count on Brightlines workmanship being among the best in the industry.</p>
    </div>
    <div class="value" style="top:398px; width:450px;">
      <h3>Innovation &amp; Technology</h3>
      <p>Customers can rely on us to apply the latest proven technologies on their projects, and to be on the ground floor of industry standards for new and emerging markets.</p>
    </div>
    <div class="value" style="top:493px; width:470px;">
      <h3>Knowledgeable &amp; Valued Employees</h3>
      <p>Brightline recognizes that its greatest asset is its people. We pledge to treat each employee with integrity, dealing honestly with all.</p>
    </div>
  </div>

  <div class="gallery__frame" style="top:38px; height:142px;">
    <span role="img" aria-label="Photo of an electrician working at a switchboard" style="background:linear-gradient(135deg,#3a5a3a,#e8e23a 55%,#cfcfcf);"></span>
  </div>
  <div class="gallery__frame" style="top:188px; height:148px;">
    <span role="img" aria-label="Photo of a solar panel array under a blue sky" style="background:linear-gradient(180deg,#b8c8d8,#2f4f8f 40%,#1a2f66);"></span>
  </div>
  <div class="gallery__frame" style="top:342px; height:148px;">
    <span role="img" aria-label="Photo of orange industrial control cabinets" style="background:linear-gradient(90deg,#6b6b6b,#e8742a 45%,#f08a30);"></span>
  </div>
  <div class="gallery__frame" style="top:494px; height:148px;">
    <span role="img" aria-label="Photo of a hand using a tablet on site" style="background:linear-gradient(135deg,#2d4d3a,#9aa0a0 50%,#e8e8e0);"></span>
  </div>

  <div class="brand">
    <div class="brand__mark"></div>
    <div class="brand__name">Brightline<br>Electrical</div>
  </div>

  <h2 class="mission__title">MISSION</h2>

  <div class="goal" style="top:642px; height:96px;">
    <div class="goal__num" style="background:var(--orange-1);">1</div>
    <div class="goal__text" style="margin-top:-2px;">
      <h3>Deliver Growth and Value By:-</h3>
      <p>Maintaining a market presence -<br>Leveraging our technical resources –<br>Networking and developing<br>stakeholder relationships</p>
    </div>
  </div>
  <div class="goal" style="top:742px; height:96px;">
    <div class="goal__num" style="background:var(--orange-2);">2</div>
    <div class="goal__text" style="margin-top:6px;">
      <h3>Remain Profitable By:-</h3>
      <p>Increasing revenue –<br>Optimizing capacity utilization –<br>Maintaining expenses</p>
    </div>
  </div>
  <div class="goal" style="top:840px; height:98px;">
    <div class="goal__num" style="background:var(--orange-3);">3</div>
    <div class="goal__text" style="margin-top:2px;">
      <h3>Be Sustainable By: -</h3>
      <p>Improving internal efficiency –<br>Diversifying our income sources –<br><span style="line-height:16px;display:inline-block;">Implementing Social &amp; Environmental improvement initiatives</span></p>
    </div>
  </div>

  <div class="statement">
    <p>Serving utilities, builders, large private and commercial clients Brightline Electrical is committed to leading the industry in safety, training and customer satisfaction.&nbsp; We will meet and exceed expectations through our full-spectrum of electrical design, build and maintenance services, state-of-the-art assets and financial strength.</p>
    <p>We will continue to embrace new technologies as they emerge and will pursue new and emerging markets. We will maintain our business beliefs and pursue unique and challenging projects to help build a culture that nurtures innovative thinking and strategic planning.</p>
  </div>

</body>
</html>
```